Convert web design from PDFs to Wordpress

I have designed the pages for my website in InDesign. I need someone to turn this into a Wordpress site. I will supply all graphics and photos and text, and the layout in PDF format.

To see PDFs of the designs we need converted to a Wordpress site, please send me an email at loricastel@mailbrook.net Thank you.

Please download PDF mockups, images, and fonts here: https://www.filecrate.net/s/kq7tmz831xpl4b2/RP%20site%20docs.zip?dl=0 After unzipping this file, you will find two folders: one for the home page, and one for the individual pages. Each folder has one PDF mockup, fonts, and linked images. Please install the included fonts so the PDF displays properly. Please see the PDF in each folder for the layout of each page. The PDFs include sticky notes with important instructions. If you previously received an email from me with PDF mockups, they are outdated: please replace those with the ones in this download link. Thank you.

This project has been completed. Not sure why Makerhive doesn't let designers know when a design has been accepted, so sorry if you didn't get the notice. Thank you for everyone who responded.

```html
<!DOCTYPE html>
<html lang="en">
<head>
<meta charset="utf-8">
<title>Rowan Pell Injury Lawyers – live site preview</title>
<link href="https://fonts.googleapis.com/css2?family=Lato:wght@400;700&family=Roboto:ital,wght@0,300;0,400;0,500;0,700;1,500&display=swap" rel="stylesheet">
<style>
:root{
  --dark:#444346;
  --dark-2:#3c3b3e;
  --gold:#c9995e;
  --ink:#333335;
  --white:#ffffff;
  --line:#dcdcdc;
  --blue:#1a6fd6;
}
*{margin:0;padding:0;box-sizing:border-box}
html,body{width:1184px;height:1200px;overflow:hidden;background:var(--white)}
body{position:relative;font-family:'Roboto',sans-serif;color:var(--ink)}
.abs{position:absolute}

/* speech bubble */
.bubble{left:54px;top:132px;width:584px;height:198px;background:var(--dark);color:var(--white);font-family:'Lato',sans-serif;text-align:center}
.bubble-line{font-size:31px;line-height:38px}
.bubble-line:first-child{margin-top:17px}
.bubble-url{font-weight:700;font-size:38px;color:var(--gold);margin-top:24px;letter-spacing:.3px}
.bubble-tail{left:0;top:0}

/* background long page */
.long-page{left:695px;top:0;width:489px;height:1200px;overflow:hidden;background:var(--white)}
.team-photo-small{left:51px;top:0;width:194px;height:140px;background:linear-gradient(180deg,#e6e6ea 0%,#5a5d6a 45%,#2d2f38 100%);border-radius:0 0 30px 30px}
.small-tag{left:63px;top:93px;width:221px;height:23px;border:1px solid #c8c8c8;text-align:center;font-size:7.5px;font-weight:700;color:var(--gold);line-height:9px;padding-top:3px}
.small-tag span{display:block;font-weight:400;color:#fff;font-size:5px;line-height:6px}
.rule-dark{left:0;top:140px;width:489px;height:4px;background:var(--dark)}
.s-title{font-weight:300;font-size:22px;color:var(--ink)}
.s-sub{font-size:8px;color:var(--gold)}
.s-text{font-size:5.2px;line-height:9.5px;color:#555}
.s-btn{height:13px;border-radius:7px;background:var(--gold);color:#fff;font-size:5px;font-weight:700;text-align:center;line-height:13px}
.band{left:0;width:489px;background:var(--dark)}
.s-head{font-size:13px;color:#fff;font-weight:400}
.s-head.dark{color:var(--ink)}
.s-list{font-size:5px;color:#e9e9e9;line-height:8.5px;text-align:center}
.s-table{border:1px solid var(--line)}
.s-row{border-bottom:1px solid var(--line);height:16px}
.field{background:#fff;height:13px;font-size:4.5px;color:#999;padding:4px 5px}
.submit{background:var(--blue);color:#fff;font-size:4px;font-weight:700;text-align:center;line-height:13px}
.office-title{font-size:8px;color:#fff}
.office-lines{font-size:5.3px;line-height:9.7px;color:#ddd}
.social-square{background:#3b5998}

/* front browser card */
.card{left:36px;top:367px;width:887px;height:656px;background:var(--white);border-radius:6px;box-shadow:0 2px 18px rgba(0,0,0,.22);overflow:hidden}
.site-header{left:0;top:0;width:887px;height:66px;background:var(--dark)}
.brand{left:0;top:0;width:248px;height:66px;text-align:center;color:#29a7e1}
.brand-name{font-size:24px;font-weight:400;margin-top:10px;line-height:26px}
.brand-tag{font-size:10px;letter-spacing:3.6px;margin-top:3px}
.divider{top:0;width:1px;height:66px;background:#6a696c}
.nav{left:302px;top:25px;font-size:11.2px;color:#fff;white-space:nowrap}
.nav span{margin-right:13px}
.nav .active{color:var(--gold)}
.call-box{left:639px;top:0;width:248px;height:66px}
.call-lead{left:48px;top:10px;font-style:italic;font-weight:500;font-size:9.6px;color:var(--gold);white-space:nowrap}
.call-phone{left:0;top:27px;width:200px;text-align:center;font-size:11px;color:#fff;margin-left:8px}
.call-lang{left:0;top:45px;width:217px;text-align:center;font-size:9.5px;color:#fff}
.serving{left:0;top:80px;width:887px;padding-right:288px;text-align:center;font-weight:500;font-size:12.2px;color:var(--ink)}
.team-photo{left:86px;top:122px;width:453px;height:266px;border-radius:40px 40px 0 0;background:linear-gradient(180deg,#f1f1f3 0%,#8a8d98 30%,#3a3d4a 70%,#2b2d36 100%)}
.photo-tag{left:110px;top:301px;width:405px;height:42px;border:1px solid #d7d7d7;text-align:center}
.photo-tag-main{font-weight:700;font-size:16px;color:var(--gold);margin-top:6px}
.photo-tag-sub{font-size:10.5px;color:#fff;margin-top:1px}
.band-rule{left:0;top:387px;width:887px;height:7px;background:var(--dark)}
.intro-title{left:70px;top:438px;font-weight:300;font-size:41px;color:var(--ink)}
.intro-sub{left:70px;top:494px;font-size:16.5px;color:var(--gold)}
.intro-rule{left:70px;top:511px;width:748px;height:1px;background:var(--gold)}
.intro-text{left:70px;top:526px;width:752px;font-size:11px;line-height:18.2px;color:var(--ink)}
.cta{left:398px;top:607px;width:91px;height:25px;border-radius:13px;background:var(--gold);color:#fff;font-size:9.5px;font-weight:700;text-align:center;line-height:25px}
</style>
</head>
<body>

<!-- background long page -->
<section class="abs long-page" aria-label="Full home page preview">
  <div class="abs team-photo-small" role="img" aria-label="Team photo of the four attorneys"></div>
  <div class="abs small-tag">Experience. Efficency. Results.<span>...and yes you can reach us by phone</span></div>
  <div class="abs rule-dark"></div>

  <h2 class="abs s-title" style="left:42px;top:162px">One Firm, two locations</h2>
  <div class="abs s-sub" style="left:42px;top:194px">ASHFORD AND LINDEN PERSONAL INJURY LAWYERS</div>
  <div class="abs" style="left:42px;top:206px;width:405px;height:1px;background:var(--gold)"></div>
  <p class="abs s-text" style="left:42px;top:214px;width:405px">Lorem ipsum dolor sit amet, consectetur adipiscing elit, sed do eiusmod tempor incididunt ut labore et dolore magna aliqua. Ut enim ad minim veniam, quis nostrud exercitation ullamco laboris nisi ut aliquip ex ea commodo consequat. Duis aute irure dolor in reprehenderit in voluptate velit esse cillum dolore eu fugiat nulla pariatur.</p>
  <div class="abs s-btn" style="left:220px;top:259px;width:49px">CONTACT US</div>

  <div class="abs band" style="top:294px;height:282px"></div>
  <h3 class="abs s-head" style="left:0;top:318px;width:489px;text-align:center">WHAT WE DO</h3>
  <div class="abs s-list" style="left:0;top:346px;width:489px">List Item #1 &nbsp;| &nbsp;List Item 2 &nbsp;| &nbsp;List Item 3 &nbsp;| &nbsp;List Item 4 &nbsp;| &nbsp;List Item5 &nbsp;| &nbsp;List Item 6 &nbsp;| &nbsp;List Item 7 &nbsp;|<br>List Item 8 &nbsp;| &nbsp;List Item 9 &nbsp;| &nbsp;List Item 10</div>
  <div class="abs s-btn" style="left:220px;top:374px;width:48px">READ MORE</div>
  <h3 class="abs s-head" style="left:128px;top:444px;white-space:nowrap">WHAT MAKES US DIFFERENT</h3>
  <p class="abs s-text" style="left:42px;top:469px;width:405px;color:#e3e3e3">Lorem ipsum dolor sit amet, consectetur adipiscing elit, sed do eiusmod tempor incididunt ut labore et dolore magna aliqua. Ut enim ad minim veniam, quis nostrud exercitation ullamco laboris nisi ut aliquip ex ea commodo consequat. Duis aute irure dolor in reprehenderit in voluptate velit esse cillum dolore eu fugiat nulla pariatur.</p>
  <p class="abs s-text" style="left:42px;top:506px;width:405px;color:#e3e3e3">Sint occaecat quis nostrud et excepteur sint occaecat cupidatat non proident</p>
  <div class="abs s-btn" style="left:210px;top:530px;width:62px">READ OUR REVIEWS</div>

  <h3 class="abs s-head dark" style="left:128px;top:600px;white-space:nowrap">WHAT MAKES US DIFFERENT</h3>
  <p class="abs s-text" style="left:150px;top:625px;white-space:nowrap">Lorem ipsum dolor sit amet, consectetur adipiscing elit.</p>
  <div class="abs s-table" style="left:42px;top:649px;width:405px;height:141px">
    <div class="s-row"></div>
    <div class="s-row" style="height:38px"><p class="s-text" style="margin:6px 0 0 185px">Ask whether the injury involved a car, premises liability insurance<br>or other coverage. The reason…</p></div>
    <div class="s-row"></div><div class="s-row"></div><div class="s-row"></div><div class="s-row"></div>
  </div>
  <div class="abs s-btn" style="left:220px;top:799px;width:48px">READ MORE</div>
  <h3 class="abs s-head dark" style="left:164px;top:857px;white-space:nowrap">REVIEWS</h3>
  <p class="abs s-text" style="left:175px;top:882px;white-space:nowrap">Hear from our awesome clients</p>

  <div class="abs band" style="top:921px;height:279px"></div>
  <h3 class="abs s-head" style="left:190px;top:956px;white-space:nowrap">CONTACT US</h3>
  <div class="abs field" style="left:250px;top:984px;width:191px">Name</div>
  <div class="abs field" style="left:250px;top:1002px;width:191px">Email</div>
  <div class="abs field" style="left:250px;top:1020px;width:191px">Phone</div>
  <div class="abs field" style="left:250px;top:1038px;width:191px;height:54px">Message</div>
  <div class="abs field" style="left:250px;top:1096px;width:191px"></div>
  <div class="abs submit" style="left:250px;top:1115px;width:26px">SUBMIT</div>

  <svg class="abs" style="left:48px;top:1035px" width="11" height="15" viewBox="0 0 11 15" aria-hidden="true"><path d="M5.5 0C2.5 0 0 2.4 0 5.4 0 9.4 5.5 15 5.5 15S11 9.4 11 5.4C11 2.4 8.5 0 5.5 0z" fill="var(--gold)"/><circle cx="5.5" cy="5.4" r="2" fill="var(--dark)"/></svg>
  <div class="abs office-title" style="left:66px;top:1036px">Ashford office</div>
  <div class="abs office-lines" style="left:66px;top:1050px">410 Alder Bend Road<br>Suite 12<br>Ashford, OR 00000<br>Tel: 555-014-2290 x1</div>
  <svg class="abs" style="left:48px;top:1096px" width="11" height="15" viewBox="0 0 11 15" aria-hidden="true"><path d="M5.5 0C2.5 0 0 2.4 0 5.4 0 9.4 5.5 15 5.5 15S11 9.4 11 5.4C11 2.4 8.5 0 5.5 0z" fill="var(--gold)"/><circle cx="5.5" cy="5.4" r="2" fill="var(--dark)"/></svg>
  <div class="abs office-title" style="left:66px;top:1098px">Linden office</div>
  <div class="abs office-lines" style="left:66px;top:1112px">88 Copper Lane<br>Suite 30<br>Linden, OR 00000<br>Tel: 555-014-2290 x2</div>
  <div class="abs social-square" style="left:46px;top:1158px;width:17px;height:17px" role="img" aria-label="Social page link"></div>
</section>

<!-- speech bubble -->
<svg class="abs bubble-tail" width="1184" height="400" aria-hidden="true"><polygon points="276,329 319,329 309,368" fill="var(--dark)"/></svg>
<div class="abs bubble">
  <p class="bubble-line">you can see your live</p>
  <p class="bubble-line">wordpress website on this url</p>
  <p class="bubble-url">https://site.pressbox-demo.net/rp</p>
</div>

<!-- front card -->
<section class="abs card" aria-label="Home page, top of screen">
  <header class="abs site-header">
    <div class="abs brand"><div class="brand-name">Rowan Pell</div><div class="brand-tag">INJURY LAWYERS</div></div>
    <div class="abs divider" style="left:248px"></div>
    <nav class="abs nav"><span class="active">HOME</span><span>WHAT WE DO</span><span>ABOUT US</span><span>FAQ</span><span>CONTACT</span></nav>
    <div class="abs divider" style="left:638px"></div>
    <div class="abs call-box">
      <div class="abs call-lead" style="left:48px">call today for your free consultation</div>
      <div class="abs call-phone" style="left:48px">(555) 014-2290</div>
      <div class="abs call-lang" style="left:48px">se habla español &nbsp;| &nbsp;讲中文</div>
    </div>
  </header>
  <div class="abs serving" style="left:0">SERVING OREGON, WASHINGTON, AND THE ENTIRE PORTLAND METRO AREA</div>
  <div class="abs team-photo" role="img" aria-label="Team photo of the four attorneys in suits"></div>
  <div class="abs photo-tag"><div class="photo-tag-main">Experience. Efficency. Results.</div><div class="photo-tag-sub">...and yes you can reach us by phone</div></div>
  <div class="abs band-rule"></div>
  <h1 class="abs intro-title">One Firm, two locations</h1>
  <h2 class="abs intro-sub" style="font-weight:400">ASHFORD AND LINDEN PERSONAL INJURY LAWYERS</h2>
  <div class="abs intro-rule"></div>
  <p class="abs intro-text">Lorem ipsum dolor sit amet, consectetur adipiscing elit, sed do eiusmod tempor incididunt ut labore et dolore magna aliqua. Ut enim ad minim veniam, quis nostrud exercitation ullamco laboris nisi ut aliquip ex ea commodo consequat. Duis aute irure dolor in reprehenderit in voluptate velit esse cillum dolore eu fugiat nulla pariatur.</p>
  <div class="abs cta">CONTACT US</div>
</section>

</body>
</html>
```